Brochure "competition" request for funds for dry toilets PMR

We would like to participate in a contest to raise funds for our associations. These funds will be used to install dry toilets accessible to people in wheelchairs in order to make an activity center attractive to people with reduced mobility. If this contest leads to a positive response, we will be able to develop the activity of cross-country skiing, walks on landscaped paths, accessibility to a picnic spot, etc...

We are located in a mountain tourist region and the objective of our association is to make as many activities as possible possible for people with disabilities.

Target Market(s)

Our project will be presented to the bank carrying out the competition

Industry/Entity Type

Tourisme de personnes en situation de handicap

Colors
EB3D1F
EC4F4E
F09395
F8D3D4
FCEDEE

Requirements
Must have
• We have a website: www.passvert-collectif.ch (still being finalized). We wish to have a bit of the same style of design as this one. Important: in the .docx file, the text is in French and it must remain so. The date of 3 days is imperative because we received the authorizations late and we have few days left to submit the project. The theme of the project is not "glamour" but necessary to allow these people to be able to practice activities. This is why it is important to obtain a presentation medium that inspires.
Nice to have
• If possible, it should be able to stay on a brochure with 4 A4 pages (= A3 horizontal double-sided)
Should not have
• It is not necessary to put too many images of illustration unrelated to the theme. We do not want medical style handicap photos, we are in tourism and we must favor the "outdoors - joie de vivre" style

```html
<!DOCTYPE html>
<html lang="fr">
<head>
<meta charset="utf-8">
<title>Passvert Collectif – Toilette sèche PMR</title>
<link href="https://fonts.googleapis.com/css2?family=Lato:ital,wght@0,400;0,700;0,900;1,400&family=Oswald:wght@500;600&display=swap" rel="stylesheet">
<style>
:root{
  --red:#e3161f;
  --red-deep:#b30d14;
  --wine:#5a0a0e;
  --wine-dark:#2e0507;
  --pink:#f09395;
  --pink-light:#f8d3d4;
  --blush:#fcedee;
  --ink:#222;
  --grey:#ececec;
  --stage:#5d5f65;
  --white:#fff;
}
*{box-sizing:border-box;margin:0;padding:0}
html,body{width:834px;height:1200px;overflow:hidden}
body{background:var(--stage);font-family:"Lato",Arial,sans-serif;color:var(--ink);position:relative}
.page{position:absolute;width:354px;height:505px;background:var(--white);overflow:hidden}
.p1{left:50px;top:82px}.p2{left:435px;top:82px}.p3{left:50px;top:615px}.p4{left:430px;top:615px;background:linear-gradient(180deg,#3a0508 0%,var(--wine) 55%,#7a0d12 100%)}
.abs{position:absolute}
.img{position:absolute}
.tab{position:absolute;background:var(--red);color:var(--white);font-weight:900;font-size:8.5px;text-transform:uppercase;display:flex;align-items:center;justify-content:center;letter-spacing:.1px}
.tab.dark{background:var(--wine)}
.h-red{color:var(--red);font-weight:900;font-size:9px}
.small{font-size:5.8px;line-height:1.35}
.frame{position:absolute;border:1.5px solid var(--red);padding:4px;background:var(--white)}
/* page 1 */
.video-band{position:absolute;left:0;top:268px;width:354px;height:19px;background:var(--red);color:var(--white);font-size:6px;font-weight:700;display:flex;align-items:center}
.video-band .label{padding-left:16px;flex:1}
.video-band .link{background:var(--wine);height:100%;width:125px;display:flex;align-items:center;padding-left:5px;font-weight:400}
.table-label{left:27px;top:294px;color:var(--white);font-weight:700;font-size:9px}
/* page 2 */
.brand{left:12px;top:12px;display:flex;align-items:center;gap:6px}
.brand-mark{width:34px;height:34px;background:var(--red)}
.brand-name{font-weight:900;font-size:11px;line-height:1.05;color:#333;text-transform:uppercase}
.hero-band{left:0;top:214px;width:354px;height:89px;background:linear-gradient(90deg,var(--red) 0%,var(--red-deep) 60%,var(--wine) 100%)}
.hero-title{right:12px;top:228px;width:200px;font-family:"Oswald",sans-serif;font-weight:600;font-size:17px;line-height:1.05;color:var(--white);text-align:center;text-transform:uppercase}
.side{left:0;top:303px;width:140px;height:202px;background:var(--wine);color:var(--white);text-align:center}
.side p{font-size:6px;line-height:1.35;font-weight:700;padding:0 14px}
.btn{display:inline-block;background:var(--red);color:var(--white);font-size:7px;font-weight:900;padding:5px 12px;margin:9px 0;text-transform:uppercase}
.members{text-align:left;font-size:5.8px;line-height:1.5;padding-left:12px;list-style:none}
.members b{font-weight:900}
.obj-box{left:152px;top:312px;width:194px;height:22px;border:1.5px solid var(--red);font-size:7px;font-weight:900;display:flex;align-items:center;justify-content:center;text-transform:uppercase}
.obj-box span{color:var(--red)}
.obj-list{left:152px;top:344px;width:195px;list-style:none}
.obj-list li{font-size:5.7px;line-height:1.35;padding-left:5px;position:relative}
.obj-list li::before{content:"";position:absolute;left:0;top:2.5px;width:2.5px;height:2.5px;border-radius:50%;background:var(--red)}
.obj-note{left:152px;top:460px;width:195px;font-size:5.7px;line-height:1.35}
/* page 3 */
.grey-area{left:0;top:0;width:227px;height:210px;background:var(--grey)}
.stat-text{left:14px;top:34px;width:200px}
.stat-text p{font-size:5.8px;line-height:1.4;margin-bottom:6px;text-align:justify}
.ref{font-size:6px;font-weight:700;line-height:1.3;margin-bottom:5px}
.ref span{color:var(--red);display:block;text-transform:uppercase}
.forces-lead{left:13px;top:242px;font-size:6.5px;font-weight:900;text-transform:uppercase}
.forces{left:13px;top:258px;width:320px;list-style:none}
.forces li{font-size:5.8px;line-height:1.3;padding-left:5px;position:relative;margin-bottom:3px}
.forces li::before{content:"";position:absolute;left:0;top:2.5px;width:2.5px;height:2.5px;border-radius:50%;background:var(--red)}
.pill{display:inline-block;border:1px solid var(--pink);border-radius:8px;padding:1.5px 6px;font-style:italic;font-size:5.5px;margin:3px 0 6px -5px;color:#333}
.pill b{font-weight:900}
.photo-band{left:0;top:411px;width:354px;height:94px;background:var(--red)}
/* page 4 */
.intro{left:0;top:37px;width:100%;text-align:center;color:var(--white);font-size:6.2px;font-weight:700;line-height:1.4}
.budget{left:42px;top:100px;width:283px;height:252px;background:var(--white)}
.budget-col{left:224px;top:100px;width:101px;height:252px;background:var(--blush)}
.budget-list{left:65px;top:135px;width:250px;list-style:none}
.budget-list li{display:flex;justify-content:space-between;font-size:6.2px;font-weight:700;margin-bottom:10px;line-height:1.35;text-transform:uppercase}
.budget-list .cost{width:55px;font-weight:400;text-align:left}
.budget-list .sub{padding-left:8px;display:block;font-weight:700}
.total{left:106px;top:321px;width:152px;height:24px;background:var(--wine);color:var(--white);font-size:8px;font-weight:700;display:flex;align-items:center;justify-content:space-between;padding:0 8px}
.total .sum{background:var(--red);height:100%;display:flex;align-items:center;padding:0 5px;margin-right:-8px}
</style>
</head>
<body>

<!-- Page 1 : dossier photo -->
<section class="page p1">
  <div class="tab dark" style="left:101px;top:0;width:149px;height:25px;background:linear-gradient(90deg,var(--wine),var(--red))">Dossier photo</div>
  <h2 class="abs h-red" style="left:16px;top:50px">1. TOILETTE SÈCHE</h2>
  <p class="abs small" style="left:16px;top:70px;width:320px">Dimensions <b>HT : Largeur 2.270 m, profondeur 1,960 m, hauteur 2,10 m</b><br>(mesures approximatives qui peuvent varier selon le choix final du fournisseur)</p>
  <div class="frame" style="left:13px;top:104px;width:104px;height:146px">
    <div role="img" aria-label="Intérieur en bois d'une toilette sèche accessible" style="width:100%;height:100%;background:linear-gradient(135deg,#c4874f,#7a5030)"></div>
  </div>
  <div role="img" aria-label="Cabane de toilette sèche en bois" class="img" style="left:129px;top:118px;width:96px;height:124px;background:linear-gradient(180deg,#a06a3c,#c88a50)"></div>
  <div class="frame" style="left:237px;top:104px;width:104px;height:146px">
    <div role="img" aria-label="Détail de la ventilation en toiture" style="width:100%;height:62px;background:linear-gradient(135deg,#8fb86a,#b07a45)"></div>
    <div role="img" aria-label="Détail du luminaire solaire sous l'avant-toit" style="width:100%;height:62px;margin-top:10px;background:linear-gradient(135deg,#c48a52,#e8d6a0)"></div>
  </div>
  <div class="video-band"><span class="label">Vidéo de présentation d'installation d'un modèle très intéressant</span><span class="link">https://video.passvert-collectif.ch/wc-pmr</span></div>
  <div role="img" aria-label="Deux personnes dont une en fauteuil roulant à une table de pique-nique accessible dans un pré" class="img" style="left:0;top:287px;width:354px;height:203px;background:linear-gradient(180deg,#7d8a5a 0%,#6a9b3e 45%,#4f8a2c 100%)"></div>
  <span class="abs table-label">2. TABLE</span>
  <div class="abs" style="left:0;top:490px;width:354px;height:15px;background:var(--red)"></div>
</section>

<!-- Page 2 : couverture -->
<section class="page p2">
  <div role="img" aria-label="Main effleurant des herbes hautes depuis un fauteuil roulant, en plein air au soleil" class="img" style="left:110px;top:0;width:244px;height:214px;background:linear-gradient(120deg,#ffffff 0%,#e8e2cf 35%,#a9a36d 70%,#5b5a3a 100%)"></div>
  <div class="abs brand"><span class="brand-mark"></span><span class="brand-name">Passvert<br>Collectif</span></div>
  <div class="abs hero-band"></div>
  <div role="img" aria-label="Cabane de toilette sèche en bois avec pictogramme d'accessibilité" class="img" style="left:6px;top:172px;width:114px;height:112px;background:linear-gradient(180deg,#8a5a32,#c98c52)"></div>
  <h1 class="abs hero-title">Installation d'une toilette sèche accessible PMR au couvert du Grand Pré-Fleuri</h1>
  <div class="abs side">
    <p style="margin-top:14px">Passvert Collectif est une association à but non lucratif crée en mai 2021.</p>
    <p style="margin-top:8px">Son siège se situe à 1899 Val-Clairon - Valais - Suisse, dans la Région Cimes du Sud (domaine des Balcons du Sud).</p>
    <span class="btn">Membres du comite</span>
    <ul class="members">
      <li><b>• Présidente :</b> Morand Élise</li>
      <li><b>• Caissier :</b> Rey-Dufour Marc</li>
      <li><b>• Secrétaire :</b> Rey-Dufour Nadia</li>
      <li><b>• Membres :</b> Crettaz Loïc</li>
      <li style="padding-left:38px">: Fellay Julien</li>
    </ul>
  </div>
  <div class="abs obj-box">Les&nbsp;<span>objectifs</span>&nbsp;de l'association sont :</div>
  <ul class="abs obj-list">
    <li>Favoriser l'accueil et les loisirs des personnes en situation de handicap</li>
    <li>Servir l'intérêt général des personnes en situation de handicap ainsi que soulager les proches aidants et accompagnants</li>
    <li>Permettre l'accès à des loisirs et l'accès à des lieux comme tout un chacun</li>
    <li>Sensibiliser et faire évoluer les représentations sociales, par des actions, communications, projets et évènements touchant et impliquant des partenaires associatifs, économiques, politiques, les médias et le public en général</li>
    <li>Favoriser la collaboration auprès des acteurs locaux</li>
  </ul>
  <p class="abs obj-note">Les ressources de l'association proviennent des cotisations, dons et manifestations organisées tout au long de l'année.</p>
</section>

<!-- Page 3 : statuts et atouts -->
<section class="page p3">
  <div class="abs grey-area"></div>
  <div role="img" aria-label="Mains en coupe remplies de pièces de monnaie" class="img" style="left:227px;top:0;width:127px;height:210px;background:linear-gradient(160deg,#f4f4f4,#d9c0a8 55%,#9b8a78)"></div>
  <div class="tab dark" style="left:0;top:0;width:145px;height:25px">Statuts de l'association</div>
  <div class="abs stat-text">
    <p class="ref">C.f. annexe 1<span>Rapport de gestion</span></p>
    <p class="ref">C.f. annexe 2<span>Présentation du projet</span></p>
    <p>Nous posons notre candidature au prix humanitaire et social de la fondation du 100ème de la BCAL pour réunir les fonds nécessaires à l'achat, l'aménagement et l'équipement spécifique d'une toilette et d'une table adaptées au couvert du Grand Pré-Fleuri à Champvert afin de rendre cet espace accessible et attractif aux personnes en situation de handicap.</p>
    <p>L'un des buts de Passvert Collectif est de permettre l'accès à des loisirs et l'accès à des lieux comme tout un chacun dans la Région Cimes du Sud. Pour y parvenir et pouvoir proposer des activités, nous nous sommes donné la mission d'équiper ce lieu ciblé qui est le point de départ de multiples activités été comme hiver.</p>
  </div>
  <div class="tab dark" style="left:0;top:210px;width:145px;height:20px;background:var(--red-deep)">Forces et atouts du projet</div>
  <p class="abs forces-lead">Lorsque ce lieu sera équipé, les personnes à mobilités réduites pourront :</p>
  <ul class="abs forces">
    <li>Partir à l'assaut de la piste de ski de fond en luge nordique<br><span class="pill"><b>https://www.cimesdusud-tourisme.ch</b>/fr/552986-ski-de-fond-grand-pre-fleuri-boucle-eclairee</span></li>
    <li>Prendre part à une agréable balade au « Chemin des poussettes »<br>qui relie le village de Champvert au Couvert<br><span class="pill"><b>https://www.cimesdusud-tourisme.ch</b>/fr/895121-chemin-des-poussettes</span></li>
    <li>Passer une agréable journée entre amis ou en famille au couvert<br><span class="pill"><b>https://www.cimesdusud-tourisme.ch</b>/fr/5310527-couvert-du-grand-pre-fleuri</span></li>
    <li>Participer à des évènements annuels divers tels que le Vélo en Fête<br><span class="pill"><b>https://www.cimesdusud-tourisme.ch</b>/fr/4941860-velo-en-fete</span></li>
  </ul>
  <div class="abs photo-band"></div>
  <div role="img" aria-label="Couvert en bois au bord d'un pré arboré" class="img" style="left:13px;top:422px;width:109px;height:76px;background:linear-gradient(180deg,#9fb5c8,#6b8a4a)"></div>
  <div role="img" aria-label="Personne en luge nordique sur une piste enneigée" class="img" style="left:122px;top:422px;width:110px;height:76px;background:linear-gradient(180deg,#c9d3de,#f2f4f6)"></div>
  <div role="img" aria-label="Balade en fauteuil sur un chemin de montagne verdoyant" class="img" style="left:232px;top:422px;width:109px;height:76px;background:linear-gradient(180deg,#7aa05a,#4e7a30)"></div>
</section>

<!-- Page 4 : infrastructures et budget -->
<section class="page p4">
  <div class="tab" style="left:107px;top:0;width:150px;height:24px">Infrastructures</div>
  <p class="abs intro">Le projet se base sur<br>• L'achat, l'aménagement et l'équipement d'une toilette adaptée<br>• L'achat d'une table en bois accessible aux personnes à mobilité réduite</p>
  <div class="abs budget"></div>
  <div class="abs budget-col"></div>
  <div class="tab" style="left:107px;top:85px;width:150px;height:30px;line-height:1.2;text-align:center">Budget d'avant projet<br>(+/-20%)</div>
  <ul class="abs budget-list">
    <li><span>1. Autorisations communales (si nécessaire)</span><span class="cost">CHF 500.-</span></li>
    <li><span>2. Installation de chantier</span><span class="cost">CHF 500.-</span></li>
    <li><span>3. Surface a goudronner (+/-10m2)</span><span class="cost">CHF 1'500.-</span></li>
    <li><span>4. Terrassement et amenagement<span class="sub">• Drain inclus</span></span><span class="cost">CHF 1'910.-</span></li>
    <li><span>5. Installation, équipements<span class="sub">• Toilette sèche PMR + urinoir extérieur</span><span class="sub">• Luminaire LED sur panneau solaire</span><span class="sub">• Système d'accès Clé-Accès</span></span><span class="cost"><br>CHF 10'000.-<br>CHF 300.-<br>CHF 300.-</span></li>
    <li><span>6. Transport, modalites douanieres<br>Buget previsionnel du WC PMR<br>Option supplementaire:</span><span class="cost">CHF 1'000.-<br>CHF 16'010.-</span></li>
    <li><span>7. Amenagement d'une table accessible en<br>fauteuil sous le couvert</span><span class="cost"><br>CHF 1800.-</span></li>
  </ul>
  <div class="abs total"><span>TOTAL PROJET</span><span class="sum">CHF 17'810.-</span></div>
  <div role="img" aria-label="Chaîne de sommets alpins teintée de rouge" class="img" style="left:0;top:395px;width:354px;height:110px;background:linear-gradient(180deg,rgba(120,10,16,0) 0%,#a3141b 45%,#5a0a0e 100%)"></div>
</section>

</body>
</html>
```